MARCO DELUCE FOR CONGRESS DISTRICT 32

I need to create a campaign flyer for my congress campaign. I am running for congress in District 32 of Texas as a civitist. I am a former Solvanic athlete, world champion fencer, Army veteran, Counterintelligence officer (I catch spies).
I want just my first name MARCO in big letters at the top. I want it to say MARCO and below it Civitist for Congress.
www.marcoforhouse.net

Political

EB3D1F
EC4F4E
F09395
F8D3D4
FCEDEE

• Would love a catchy title for the Flyer like "Spy Catcher", "Solvanic Athlete" "World Champion Fencer" running for Congress in your District!

```html
<!DOCTYPE html>
<html lang="en">
<head>
<meta charset="utf-8">
<title>Marco for Congress – Flyer</title>
<link rel="stylesheet" href="https://fonts.googleapis.com/css2?family=Righteous&family=Rubik:wght@600;700;800&family=Roboto:wght@400;500;700&display=swap">
<style>
  :root {
    --stage: #d9d9d9;
    --navy: #21347c;
    --violet: #4a2a6e;
    --crimson: #b1223a;
    --yellow: #fff200;
    --banner-red: #d8202f;
    --white: #ffffff;
    --logo-red: #d8202f;
    --skin: #c79a86;
    --shirt: #e6e8ee;
    --illustration: #e8a1a6;
  }
  * { margin: 0; padding: 0; box-sizing: border-box; }
  html, body {
    width: 1200px; height: 2652px; overflow: hidden;
    background: var(--stage);
  }
  .flyer {
    position: absolute; left: 60px; top: 568px;
    width: 1080px; height: 1516px; overflow: hidden;
    background: linear-gradient(160deg, var(--navy) 0%, #2f2f78 30%, var(--violet) 55%, #7a2550 78%, var(--crimson) 100%);
    color: var(--white);
    font-family: "Roboto", sans-serif;
  }
  .first-name {
    position: absolute; left: 0; top: 64px; width: 100%;
    text-align: center; white-space: nowrap;
    font-family: "Righteous", sans-serif; font-weight: 400;
    font-size: 278px; line-height: 1;
    letter-spacing: -4px;
    color: var(--yellow);
    transform: scaleY(1.3);
    transform-origin: 50% 14%;
  }
  .party-banner {
    position: absolute; left: 215px; top: 444px; width: 653px; height: 64px;
  }
  .party-banner svg { position: absolute; inset: 0; }
  .party-banner span {
    position: absolute; inset: 0;
    display: flex; align-items: center; justify-content: center;
    font-family: "Righteous", sans-serif; font-size: 40px;
    color: var(--white); letter-spacing: 1px;
  }
  .headline {
    position: absolute; left: 0; width: 100%; text-align: center;
    font-family: "Rubik", sans-serif; color: var(--yellow); white-space: nowrap;
  }
  .headline-district { top: 541px; font-size: 62px; font-weight: 700; line-height: 1.1; }
  .headline-countdown { top: 603px; font-size: 90px; font-weight: 800; line-height: 1.05; }
  .subline {
    position: absolute; left: 0; top: 695px; width: 100%;
    text-align: center; font-size: 21px; font-weight: 500; line-height: 25px;
  }
  .letter { position: absolute; left: 60px; top: 776px; width: 520px; z-index: 2; }
  .letter h2 {
    font-family: "Rubik", sans-serif; font-weight: 700;
    font-size: 40px; color: var(--yellow); line-height: 1.1;
  }
  .letter p { font-size: 21px; line-height: 25.4px; margin-top: 4px; white-space: nowrap; }
  .megaphone-art {
    position: absolute; left: 0; top: 972px; width: 328px; height: 392px;
    background: radial-gradient(ellipse at 60% 35%, var(--illustration) 0%, rgba(216,32,47,0.55) 45%, rgba(120,20,40,0) 75%);
  }
  .support { position: absolute; left: 249px; top: 1150px; width: 380px; z-index: 2; }
  .support h3 {
    font-family: "Righteous", sans-serif; font-weight: 400;
    font-size: 16px; letter-spacing: 0.5px; margin-bottom: 12px; white-space: nowrap;
  }
  .support p { font-size: 23px; line-height: 29px; white-space: nowrap; }
  .support strong { font-weight: 700; }
  .support .gap { margin-top: 4px; }
  .name-plate {
    position: absolute; left: 60px; top: 1383px; width: 570px; height: 107px;
    background: var(--white); border-radius: 53px 0 0 53px;
    display: flex; align-items: center; padding-left: 58px;
  }
  .name-plate span {
    font-family: "Rubik", sans-serif; font-weight: 800;
    font-size: 27px; line-height: 1.1; color: var(--logo-red);
  }
  .candidate-photo {
    position: absolute; left: 635px; top: 790px; width: 445px; height: 726px;
    border-radius: 200px 200px 0 0;
    background: linear-gradient(180deg, #5a4038 0%, var(--skin) 22%, #d8b3a2 45%, var(--shirt) 62%, #f3f4f7 100%);
  }
</style>
</head>
<body>
  <main class="flyer">
    <h1 class="first-name">MARCO</h1>

    <div class="party-banner">
      <svg width="653" height="64" viewBox="0 0 653 64" aria-hidden="true">
        <polygon points="0,32 14,0 28,32 14,64" fill="#fff200"/>
        <polygon points="625,32 639,0 653,32 639,64" fill="#fff200"/>
        <polygon points="34,4 619,4 608,60 45,60" fill="#d8202f"/>
      </svg>
      <span>CIVITIST FOR CONGRESS</span>
    </div>

    <p class="headline headline-district">PRIMARY DISTRICT TX-32 2026</p>
    <p class="headline headline-countdown">COUNTDOWN!</p>
    <p class="subline">The date is approaching fast and we’re making<br>preparations. Don’t miss out!</p>

    <section class="letter">
      <h2>DEAR TEXANS,</h2>
      <p>I'm not a rich millionaire with self-interests like other<br>Candidates. I come from nothing, and my<br>parents worked hard to give me a chance to fight<br>for my career. I'm a Veteran. Solvanic<br>Athlete. Family man.&nbsp; I love my country. I am here<br>to earn your vote".</p>
    </section>

    <div class="megaphone-art" role="img" aria-label="Illustration of a hand raising a red and pink megaphone"></div>

    <div class="candidate-photo" role="img" aria-label="Portrait photo of the candidate smiling in a white patterned shirt"></div>

    <section class="support">
      <h3>SUPPORT MARCO DELUCE FOR CONGRESS</h3>
      <p>If you prefer <strong>QUIKPAY:</strong><br>hello@marcoforhouse.net</p>
      <p class="gap">or mail a check to: MARCO DELUCE<br>FOR CONGRESS<br>4417 Larkspur Ln. Garland,<br>TX 75040</p>
    </section>

    <div class="name-plate"><span>MARCO DELUCE<br>FOR CONGRESS TEXAS-32</span></div>
  </main>
</body>
</html>
```